bramblecrest paving card makeover

were a excavation/paving contractor from Monterey ca, I'm looking to have a card designed front and back that has company details on the front and a list of the services we offer on the back.

Target Market(s)

home owners property management companies

Industry/Entity Type

Contractor

Contact Information for Business Card

bramblecrest paving 418 larkmoor st Monterey ca. licensed, insured and bonded
lic#657920 gerald pinsky operations manager

Font styles to use
Serif
Sans Serif

Colors
f78f20

Requirements
Must have
• a list of my services on back, asphalt construction and maintenance, drainage, foundations, retaining walls, chip seals, excavation, grading, landscape ground work, interlocking paver, hydro-seeding, structured and driveway demolition, utility trenching and stump removal.
Nice to have
• my new domain and page address I'm acquiring from pixel bazaar.

```html
<!DOCTYPE html>
<html lang="en">
<head>
<meta charset="utf-8">
<title>Bramblecrest Paving – Business Card</title>
<link href="https://fonts.googleapis.com/css2?family=Lato:wght@400;700;900&display=swap" rel="stylesheet">
<style>
  :root {
    --backdrop: #efedeb;
    --card: #282828;
    --ink-light: #ffffff;
    --ink-soft: #e6e6e6;
    --mark-bg: #ffffff;
    --mark-ink: #282828;
  }
  * { box-sizing: border-box; margin: 0; padding: 0; }
  html, body { width: 1200px; height: 900px; overflow: hidden; }
  body {
    background: var(--backdrop);
    font-family: "Lato", Arial, sans-serif;
    position: relative;
  }
  .card {
    position: absolute;
    background: var(--card);
    border-radius: 14px;
    color: var(--ink-light);
    overflow: hidden;
  }
  .card--front { left: 178px; top: 74px; width: 588px; height: 364px; }
  .card--back  { left: 390px; top: 505px; width: 565px; height: 351px; }

  .brand-disc {
    position: absolute;
    border-radius: 50%;
    background: var(--mark-bg);
    display: flex;
    align-items: center;
    justify-content: center;
    text-align: center;
  }
  .card--front .brand-disc { left: 272px; top: 29px; width: 304px; height: 304px; }
  .card--back  .brand-disc { left: 28px; top: 30px; width: 290px; height: 290px; }
  .brand-name {
    color: var(--mark-ink);
    font-weight: 900;
    font-size: 34px;
    line-height: 1.1;
    letter-spacing: 1px;
    text-transform: uppercase;
  }

  .contact { position: absolute; left: 22px; top: 50px; }
  .contact__name { font-size: 21px; font-weight: 700; text-transform: uppercase; letter-spacing: .3px; line-height: 1; }
  .contact__role { font-size: 16px; color: var(--ink-soft); margin-top: 5px; }
  .contact__licence { font-size: 16px; color: var(--ink-soft); margin-top: 20px; }
  .contact__lines { list-style: none; margin-top: 12px; }
  .contact__lines li { font-size: 16px; color: var(--ink-soft); line-height: 22px; display: flex; align-items: center; gap: 5px; }
  .contact__lines svg { width: 13px; height: 13px; fill: var(--ink-light); }
  .contact__company { font-size: 14px; color: var(--ink-soft); text-transform: uppercase; margin-top: 13px; }
  .contact__address { font-size: 17px; color: var(--ink-soft); margin-top: 3px; }
  .contact__tagline {
    font-size: 17px; font-weight: 700; letter-spacing: 1.3px; text-transform: uppercase;
    line-height: 22px; margin-top: 19px; width: 260px;
  }

  .services {
    position: absolute; right: 26px; top: 30px;
    list-style: none; text-align: right;
  }
  .services li { font-size: 16px; line-height: 20.5px; color: var(--ink-soft); padding-right: 14px; position: relative; }
  .services li.bullet::after {
    content: ""; position: absolute; right: 0; top: 8px;
    width: 6px; height: 6px; border-radius: 50%; background: var(--ink-light);
  }
</style>
</head>
<body>

<section class="card card--front" aria-label="Card front">
  <div class="contact">
    <p class="contact__name">Dorian Kessel</p>
    <p class="contact__role">Managing Director</p>
    <p class="contact__licence">Lic# 657920</p>
    <ul class="contact__lines">
      <li><svg viewBox="0 0 16 16" aria-hidden="true"><path d="M2 4c0-2 2-3 6-3s6 1 6 3v1h-3V3.5H5V5H2zM4 7h8l2 6v2H2v-2zM8 9a2 2 0 100 4 2 2 0 000-4z"/></svg>555 310 7742</li>
      <li><svg viewBox="0 0 16 16" aria-hidden="true"><path d="M1 3h14v10H1zM2 4.5v.5l6 4 6-4v-.5z"/></svg>info@bramblecrestmail.com</li>
      <li><svg viewBox="0 0 16 16" aria-hidden="true"><circle cx="8" cy="8" r="7"/><path d="M5 4c2 1 1 3 3 3s1 3 3 4" stroke="#282828" stroke-width="1.4" fill="none"/></svg>www.bramblecrestsite.com</li>
    </ul>
    <p class="contact__company">Bramblecrest Paving</p>
    <p class="contact__address">418 larkmoor st Monterey ca.</p>
    <p class="contact__tagline">Licensed, insured and bonded</p>
  </div>
  <div class="brand-disc"><span class="brand-name">Bramblecrest<br>Paving</span></div>
</section>

<section class="card card--back" aria-label="Card back">
  <div class="brand-disc"><span class="brand-name">Bramblecrest<br>Paving</span></div>
  <ul class="services">
    <li class="bullet">Asphalt construction</li>
    <li>and maintenance</li>
    <li class="bullet">Drainage</li>
    <li class="bullet">Foundations</li>
    <li class="bullet">Retaining walls</li>
    <li class="bullet">Chip seals</li>
    <li class="bullet">Excavation</li>
    <li class="bullet">Grading</li>
    <li class="bullet">Landscape ground work</li>
    <li class="bullet">Interlocking paver</li>
    <li class="bullet">Hydro-seeding</li>
    <li class="bullet">Structured and</li>
    <li>driveway demolition</li>
    <li class="bullet">Utility trenching and stump removal</li>
  </ul>
</section>

</body>
</html>
```